Brookfield Medical Centre is a Covid-19 Secure and PMV approved facility. It is a multi-specialty medical clinic offering consultations and treatments across various specialties. We offer services to private as well as TAR patients.

```html
<!DOCTYPE html>
<html lang="en">
<head>
<meta charset="utf-8">
<title>Brookfield Medical Centre – Covid 19 Secure Facility</title>
<link href="https://fonts.googleapis.com/css2?family=Montserrat:wght@500;600;700&family=Poppins:wght@600;700&display=swap" rel="stylesheet">
<style>
  :root {
    --navy: #2a2376;
    --blue: #1a7fd1;
    --sky: #cfe3f0;
    --panel: #ebebef;
    --ink: #1e1e2a;
    --white: #ffffff;
    --badge: #e8a53a;
  }
  * { margin: 0; padding: 0; box-sizing: border-box; }
  html, body { width: 800px; height: 1200px; overflow: hidden; background: #ffffff; }
  .flyer {
    position: relative; width: 800px; height: 1200px; overflow: hidden;
    background: var(--white); font-family: "Montserrat", sans-serif; color: var(--ink);
  }
  .brand {
    position: absolute; left: 56px; top: 62px;
    font-family: "Montserrat", sans-serif; font-weight: 600; font-size: 22px;
    color: var(--navy); line-height: 1.1; display: flex; align-items: center; gap: 10px;
  }
  .brand-dot { width: 14px; height: 14px; border-radius: 50%; background: var(--navy); }
  .rule-top { position: absolute; left: 0; top: 128px; width: 800px; height: 3px; background: var(--blue); }
  .rule-top-thick { position: absolute; left: 430px; top: 124px; width: 370px; height: 8px; background: var(--blue); }
  .hero {
    position: absolute; left: 0; top: 142px; width: 800px; height: 311px;
    background: linear-gradient(120deg, #b9d6e8 0%, #dbeaf3 45%, #a9c9de 100%);
  }
  .hero-team {
    position: absolute; left: 430px; top: 32px; width: 340px; height: 421px;
    background: linear-gradient(180deg, #e9eef2 0%, #dfe7ee 60%, #cfdde8 100%);
    border-radius: 120px 120px 0 0;
  }
  .headline {
    position: absolute; left: 42px; display: block; white-space: nowrap;
    font-family: "Poppins", sans-serif; font-weight: 700; font-size: 46px;
    color: var(--white); line-height: 62px; padding: 0 12px; letter-spacing: 0.5px;
  }
  .headline-1 { top: 207px; width: 305px; background: var(--navy); }
  .headline-2 { top: 278px; width: 250px; background: var(--navy); }
  .headline-3 { top: 350px; width: 305px; background: var(--blue); }
  .hero-base { position: absolute; left: 0; top: 453px; width: 800px; height: 16px; }
  .building {
    position: absolute; left: 417px; top: 488px; width: 383px; height: 262px;
    background: linear-gradient(180deg, #d6dbe1 0%, #56647a 40%, #3a4456 100%);
  }
  .section-title {
    position: absolute; left: 41px; font-family: "Poppins", sans-serif; font-weight: 600;
    font-size: 23px; color: var(--ink); letter-spacing: .5px;
  }
  .section-title span { color: var(--blue); }
  .section-title::after {
    content: ""; position: absolute; left: 0; top: 38px; width: 70px; height: 2px; background: var(--navy);
  }
  .title-public { top: 494px; }
  .title-private { top: 686px; }
  .public-service {
    position: absolute; display: flex; align-items: center; gap: 10px;
    font-weight: 600; font-size: 19px; color: var(--ink); white-space: nowrap;
  }
  .public-icon { width: 40px; height: 40px; border-radius: 50%; display: block; }
  .private-panel { position: absolute; left: 0; top: 750px; width: 800px; height: 243px; background: var(--panel); }
  .private-col { position: absolute; top: 780px; list-style: none; }
  .private-col li {
    display: flex; align-items: flex-start; gap: 14px; font-size: 17px; font-weight: 500;
    line-height: 20px; margin-bottom: 21px; color: var(--ink);
  }
  .private-col li::before {
    content: ""; flex: none; width: 10px; height: 10px; border-radius: 50%;
    background: var(--navy); margin-top: 5px;
  }
  .col-1 { left: 44px; }
  .col-2 { left: 326px; }
  .col-3 { left: 584px; }
  .divider { position: absolute; top: 772px; width: 2px; height: 200px; background: #dcdce2; }
  .hours-icon { position: absolute; left: 42px; top: 1030px; }
  .hours-label {
    position: absolute; left: 106px; top: 1016px; font-family: "Poppins", sans-serif;
    font-weight: 600; font-size: 25px; color: var(--navy); line-height: 34px;
  }
  .hours-time {
    position: absolute; left: 106px; top: 1050px; font-family: "Poppins", sans-serif;
    font-weight: 600; font-size: 29px; color: var(--ink); line-height: 40px;
  }
  .days-button {
    position: absolute; left: 407px; top: 1017px; width: 352px; height: 64px;
    background: var(--blue); border-radius: 22px; color: var(--white);
    font-family: "Poppins", sans-serif; font-weight: 600; font-size: 27px;
    display: flex; align-items: center; justify-content: center; letter-spacing: 1px;
  }
  .footer { position: absolute; left: 0; top: 1107px; width: 800px; height: 93px; }
  .contact {
    position: absolute; display: flex; align-items: center; gap: 8px;
    color: var(--white); font-size: 12.5px; font-weight: 500; white-space: nowrap;
  }
  .contact-phone { left: 52px; top: 1127px; font-size: 20px; font-weight: 700; }
  .contact-address { left: 52px; top: 1154px; }
  .contact-email { left: 392px; top: 1129px; }
  .contact-web { left: 392px; top: 1152px; }
</style>
</head>
<body>
<main class="flyer">

  <div class="brand"><span class="brand-dot"></span>Brookfield Medical Centre</div>

  <div class="rule-top"></div>
  <div class="rule-top-thick"></div>

  <div class="hero" role="img" aria-label="Photo of a modern hospital corridor with light blue digital overlay"></div>
  <div class="hero-team" role="img" aria-label="Photo of two clinicians in masks and white coats with arms crossed"></div>

  <h1>
    <span class="headline headline-1">A COVID 19</span>
    <span class="headline headline-2">SECURE</span>
    <span class="headline headline-3">FACILITY</span>
  </h1>

  <svg class="hero-base" viewBox="0 0 800 16" aria-hidden="true">
    <rect x="0" y="6" width="800" height="10" fill="#1a7fd1"/>
    <polygon points="0,0 270,0 290,6 0,6" fill="#1a7fd1"/>
    <rect x="0" y="12" width="800" height="4" fill="#ffffff"/>
    <rect x="0" y="13" width="800" height="3" fill="#1a7fd1"/>
  </svg>

  <div class="building" role="img" aria-label="Photo of the medical centre building with a glass frontage"></div>

  <h2 class="section-title title-public">TAR <span>SERVICES</span></h2>

  <div class="public-service" style="left:41px;top:562px">
    <svg class="public-icon" viewBox="0 0 40 40" aria-hidden="true"><circle cx="20" cy="20" r="20" fill="#1a7fd1"/><circle cx="20" cy="18" r="7" fill="none" stroke="#fff" stroke-width="2"/><path d="M20 25v7M16 29h8" stroke="#fff" stroke-width="2"/></svg>
    Gynaecology
  </div>
  <div class="public-service" style="left:230px;top:562px">
    <svg class="public-icon" viewBox="0 0 40 40" aria-hidden="true"><circle cx="20" cy="20" r="20" fill="#2a2376"/><path d="M20 10c-4 6-5 8-5 10a5 5 0 0 0 10 0c0-2-1-4-5-10z" fill="none" stroke="#fff" stroke-width="2"/><path d="M10 28h20M12 32h16" stroke="#fff" stroke-width="1.5"/></svg>
    Dermatology
  </div>
  <div class="public-service" style="left:41px;top:617px">
    <svg class="public-icon" viewBox="0 0 40 40" aria-hidden="true"><circle cx="20" cy="20" r="20" fill="#2a2376"/><path d="M8 20q12-11 24 0q-12 11-24 0z" fill="none" stroke="#fff" stroke-width="2"/><circle cx="20" cy="20" r="4" fill="#fff"/></svg>
    Eye Clinic
  </div>
  <div class="public-service" style="left:230px;top:617px">
    <svg class="public-icon" viewBox="0 0 40 40" aria-hidden="true"><circle cx="20" cy="20" r="20" fill="#1a7fd1"/><rect x="12" y="16" width="16" height="14" fill="none" stroke="#fff" stroke-width="2"/><path d="M20 8v6M17 11h6" stroke="#fff" stroke-width="2"/></svg>
    ENT Clinic
  </div>

  <h2 class="section-title title-private">PRIVATE <span>SERVICES</span></h2>

  <section class="private-panel"></section>
  <div class="divider" style="left:262px"></div>
  <div class="divider" style="left:521px"></div>

  <ul class="private-col col-1">
    <li>Eye Clinic</li>
    <li>GP</li>
    <li>Gynaecology</li>
    <li>Physiotherapy</li>
    <li>Reflexology</li>
  </ul>
  <ul class="private-col col-2">
    <li>Urology</li>
    <li>Counselling</li>
    <li>Dermatology</li>
    <li>ENT (Incl<br>Microsuction)</li>
    <li>Dental</li>
  </ul>
  <ul class="private-col col-3">
    <li>Chiropractor</li>
    <li>Orthopaedics</li>
    <li>General<br>Medicine</li>
    <li>Neurology</li>
  </ul>

  <svg class="hours-icon" width="50" height="48" viewBox="0 0 50 48" aria-hidden="true">
    <rect x="2" y="6" width="38" height="34" rx="3" fill="none" stroke="#1a7fd1" stroke-width="2.5"/>
    <path d="M2 14h38" stroke="#1a7fd1" stroke-width="2.5"/>
    <path d="M10 2v8M18 2v8M26 2v8M34 2v8" stroke="#1a7fd1" stroke-width="2"/>
    <g fill="#1a7fd1"><rect x="8" y="19" width="5" height="4"/><rect x="16" y="19" width="5" height="4"/><rect x="24" y="19" width="5" height="4"/><rect x="8" y="27" width="5" height="4"/><rect x="16" y="27" width="5" height="4"/></g>
    <circle cx="38" cy="36" r="10" fill="#fff" stroke="#1a7fd1" stroke-width="2.5"/>
    <path d="M38 30v6h4" fill="none" stroke="#1a7fd1" stroke-width="2"/>
  </svg>
  <p class="hours-label">OPENING HOURS</p>
  <p class="hours-time">8.00AM — 8.00PM</p>
  <div class="days-button">MONDAY TO SUNDAY</div>

  <svg class="footer" viewBox="0 0 800 93" aria-hidden="true">
    <rect x="0" y="0" width="800" height="93" fill="#2a2376"/>
    <polygon points="595,0 800,0 800,60 665,60" fill="#ffffff"/>
    <polygon points="600,0 612,0 672,52 800,52 800,60 665,60" fill="#1a7fd1"/>
    <rect x="640" y="74" width="160" height="6" fill="#1a7fd1"/>
    <circle cx="712" cy="28" r="18" fill="#e8a53a"/>
  </svg>

  <div class="contact contact-phone">
    <svg width="14" height="14" viewBox="0 0 24 24" aria-hidden="true"><path d="M6.6 10.8a15 15 0 0 0 6.6 6.6l2.2-2.2a1 1 0 0 1 1-.25 11.4 11.4 0 0 0 3.6.57 1 1 0 0 1 1 1V20a1 1 0 0 1-1 1A17 17 0 0 1 3 4a1 1 0 0 1 1-1h3.5a1 1 0 0 1 1 1c0 1.25.2 2.45.57 3.57a1 1 0 0 1-.25 1z" fill="#1a7fd1"/></svg>
    01632 960418
  </div>
  <div class="contact contact-address">
    <svg width="12" height="14" viewBox="0 0 24 28" aria-hidden="true"><path d="M12 0a10 10 0 0 0-10 10c0 7.5 10 18 10 18s10-10.5 10-18A10 10 0 0 0 12 0zm0 14a4 4 0 1 1 0-8 4 4 0 0 1 0 8z" fill="#1a7fd1"/></svg>
    Brookfield Avenue, Millbrook, Eastshire, MB4 7QT
  </div>
  <div class="contact contact-email">
    <svg width="12" height="10" viewBox="0 0 24 18" aria-hidden="true"><rect x="0" y="0" width="24" height="18" rx="2" fill="#1a7fd1"/><path d="M1 2l11 8 11-8" fill="none" stroke="#2a2376" stroke-width="2"/></svg>
    admin@brookfieldmc.example
  </div>
  <div class="contact contact-web">
    <svg width="12" height="12" viewBox="0 0 24 24" aria-hidden="true"><circle cx="12" cy="12" r="11" fill="#1a7fd1"/><path d="M1 12h22M12 1c4 4 4 18 0 22M12 1c-4 4-4 18 0 22" fill="none" stroke="#2a2376" stroke-width="1.5"/></svg>
    www.brookfieldmc.example
  </div>

</main>
</body>
</html>
```